Paulette 2

This project is a continuation of the previous "Paulette".

We would like a mix of the two joined images:
- the night-club: background
- the lady: or, better a drawing from this photo

Cover 14 x 20.5 cm (vertical)
Author: La baronne Solène Marquet (should be at the top)
Title: Paulette's umbrellas
Publisher: Editions Pivolet (should be at the bottom)

The book is a humorous story of a fat woman, with a sturdy character.
The text is the adventure story of this big woman who leaves the country and moves to a city and works as a toilet employee in a "chic" cabaret.

Besoin de quelques jours pour choisir un design

```html
<!DOCTYPE html>
<html lang="fr">
<head>
<meta charset="utf-8">
<title>Les Parapluies de Paulette — couverture</title>
<link rel="stylesheet" href="https://fonts.googleapis.com/css2?family=Bodoni+Moda:opsz,wght@6..96,500;6..96,700&family=Poiret+One&display=swap">
<style>
  :root {
    --page-bg: #f3f3f4;
    --night-blue: #33329a;
    --deep-indigo: #26287c;
    --club-shadow: #1d1f66;
    --violet: #5b2fa0;
    --magenta: #c8168c;
    --hot-pink: #e0209a;
    --ice-blue: #6fb4ea;
    --glow: #f4f1fb;
    --ink-light: #ffffff;
  }
  * { margin: 0; padding: 0; box-sizing: border-box; }
  html, body {
    width: 1200px;
    height: 815px;
    overflow: hidden;
    background: var(--page-bg);
  }
  .stage {
    position: relative;
    width: 1200px;
    height: 815px;
  }
  .book-cover {
    position: absolute;
    left: 354px;
    top: 47px;
    width: 492px;
    height: 720px;
    overflow: hidden;
    background: var(--night-blue);
  }
  .cover-artwork {
    position: absolute;
    inset: 0;
    width: 100%;
    height: 100%;
  }
  .author {
    position: absolute;
    left: 72px;
    top: 50px;
    font-family: "Bodoni Moda", "Didot", serif;
    font-weight: 500;
    font-size: 50px;
    line-height: 1;
    color: var(--ink-light);
    white-space: nowrap;
    transform: scaleX(0.48);
    transform-origin: left top;
  }
  .title {
    position: absolute;
    left: 70px;
    top: 96px;
    font-family: "Poiret One", "Futura", sans-serif;
    font-weight: 400;
    font-size: 64px;
    line-height: 62px;
    color: var(--ink-light);
    text-transform: uppercase;
    white-space: nowrap;
    -webkit-text-stroke: 1.8px var(--ink-light);
  }
  .title-line { display: block; }
  .publisher {
    position: absolute;
    left: 70px;
    right: 68px;
    top: 670px;
    display: flex;
    justify-content: space-between;
    font-family: "Bodoni Moda", "Didot", serif;
    font-weight: 700;
    font-size: 26px;
    line-height: 1;
    color: var(--ink-light);
    transform: scaleY(1.1);
  }
  .publisher .gap { width: 28px; }
</style>
</head>
<body>
<main class="stage">
  <section class="book-cover" aria-label="Couverture du livre">
    <svg class="cover-artwork" viewBox="0 0 492 720" preserveAspectRatio="none" role="img" aria-label="Photographie de couverture : une femme corpulente croquant une tablette de chocolat, au premier plan d'une boîte de nuit baignée de lumières bleues et roses">
      <defs>
        <linearGradient id="club-backdrop" x1="0" y1="0" x2="0" y2="1">
          <stop offset="0" stop-color="var(--club-shadow)"/>
          <stop offset="0.16" stop-color="var(--deep-indigo)"/>
          <stop offset="0.4" stop-color="var(--night-blue)"/>
          <stop offset="0.75" stop-color="var(--violet)"/>
          <stop offset="1" stop-color="var(--night-blue)"/>
        </linearGradient>
        <radialGradient id="white-light">
          <stop offset="0" stop-color="var(--glow)" stop-opacity="1"/>
          <stop offset="0.45" stop-color="var(--glow)" stop-opacity="0.7"/>
          <stop offset="1" stop-color="var(--glow)" stop-opacity="0"/>
        </radialGradient>
        <radialGradient id="pink-light">
          <stop offset="0" stop-color="var(--hot-pink)" stop-opacity="0.95"/>
          <stop offset="0.55" stop-color="var(--magenta)" stop-opacity="0.6"/>
          <stop offset="1" stop-color="var(--magenta)" stop-opacity="0"/>
        </radialGradient>
        <radialGradient id="blue-light">
          <stop offset="0" stop-color="var(--ice-blue)" stop-opacity="0.8"/>
          <stop offset="1" stop-color="var(--ice-blue)" stop-opacity="0"/>
        </radialGradient>
        <radialGradient id="shadow-pool">
          <stop offset="0" stop-color="var(--club-shadow)" stop-opacity="0.7"/>
          <stop offset="1" stop-color="var(--club-shadow)" stop-opacity="0"/>
        </radialGradient>
      </defs>
      <rect width="492" height="720" fill="url(#club-backdrop)"/>
      <!-- club ceiling lights -->
      <ellipse cx="86" cy="18" rx="40" ry="22" fill="url(#pink-light)" opacity="0.6"/>
      <ellipse cx="360" cy="40" rx="120" ry="45" fill="url(#blue-light)" opacity="0.25"/>
      <!-- blurred crowd lights -->
      <ellipse cx="108" cy="330" rx="50" ry="70" fill="url(#blue-light)"/>
      <ellipse cx="20" cy="300" rx="30" ry="50" fill="url(#blue-light)" opacity="0.5"/>
      <!-- spotlight beams -->
      <ellipse cx="470" cy="260" rx="40" ry="110" fill="url(#pink-light)" opacity="0.7"/>
      <ellipse cx="470" cy="680" rx="150" ry="110" fill="url(#pink-light)"/>
      <!-- lit figure -->
      <ellipse cx="250" cy="400" rx="130" ry="170" fill="url(#white-light)"/>
      <ellipse cx="235" cy="610" rx="150" ry="90" fill="url(#white-light)" opacity="0.9"/>
      <ellipse cx="400" cy="430" rx="80" ry="160" fill="url(#shadow-pool)"/>
      <ellipse cx="80" cy="560" rx="120" ry="80" fill="url(#pink-light)"/>
      <ellipse cx="200" cy="520" rx="110" ry="90" fill="url(#pink-light)" opacity="0.75"/>
      <ellipse cx="150" cy="710" rx="190" ry="50" fill="url(#pink-light)" opacity="0.6"/>
    </svg>

    <p class="author">La baronne Solène Marquet</p>
    <h1 class="title">
      <span class="title-line">Les Parapluies</span>
      <span class="title-line">de Paulette</span>
    </h1>
    <p class="publisher" aria-label="Editions Pivolet">
      <span>E</span><span>D</span><span>I</span><span>T</span><span>I</span><span>O</span><span>N</span><span>S</span><span class="gap"></span><span>P</span><span>I</span><span>V</span><span>O</span><span>L</span><span>E</span><span>T</span>
    </p>
  </section>
</main>
</body>
</html>
```